Carver Lindqvist Group Business Cards

We have a new logo, and want to design new business cards with it. We are 21 years in business, and want a fresh but professional look, so not a lot of extra stuff on the card. We are a recruiting and staffing firm focused on placing accounting and finance professionals in the Dallas TX area. I've attached our new logo that should be displayed on the cards. Here is what I think we want on the cards:
Ray Pemberly, CPA
Partner and Managing Director
8282 Orchard Vale Rd.
Suite 610
Dallas, TX 75391
O 214-555-0184
M 214-555-0237
ray@carverlindqvist.example
www.carverlindqvist.example

```html
<!DOCTYPE html>
<html lang="en">
<head>
<meta charset="utf-8">
<title>Carver Lindqvist Group — Business Cards</title>
<link rel="stylesheet" href="https://fonts.googleapis.com/css2?family=PT+Sans:wght@400;700&family=Roboto+Condensed:wght@700&display=swap">
<style>
  :root {
    --page-bg: #ecebe8;
    --card-bg: #f7f7f8;
    --pattern-a: #f9f9fa;
    --pattern-b: #e9e9ec;
    --brand-blue: #5470bd;
    --ink-blue: #1f3d9c;
    --white: #ffffff;
  }
  * { box-sizing: border-box; margin: 0; padding: 0; }
  html, body { width: 1200px; height: 900px; overflow: hidden; }
  body {
    background: var(--page-bg);
    display: flex;
    align-items: center;
    justify-content: center;
    gap: 40px;
    font-family: "PT Sans", Arial, sans-serif;
  }
  .card {
    position: relative;
    width: 540px;
    height: 310px;
    background: var(--card-bg);
    overflow: hidden;
    box-shadow: 0 10px 24px rgba(0,0,0,0.18);
  }
  .card-texture {
    position: absolute;
    inset: 0;
    background: linear-gradient(135deg, var(--pattern-a) 0%, var(--pattern-b) 35%, var(--pattern-a) 60%, var(--pattern-b) 100%);
  }
  .edge-bar {
    position: absolute;
    width: 22px;
    height: 94px;
    background: var(--brand-blue);
  }
  .edge-bar--right { right: 0; top: 74px; }
  .edge-bar--left { left: 0; bottom: 56px; }
  .brand-name {
    position: absolute;
    display: flex;
    align-items: center;
    gap: 10px;
    font-family: "PT Sans", Arial, sans-serif;
    font-weight: 700;
    text-transform: uppercase;
    letter-spacing: 0.5px;
    line-height: 1.05;
  }
  .brand-mark { width: 14px; height: 14px; flex: none; }
  .card--front .brand-name {
    left: 50%; top: 50%;
    transform: translate(-50%, -50%);
    color: var(--ink-blue);
    font-size: 21px;
    white-space: nowrap;
  }
  .card--front .brand-mark { background: var(--ink-blue); }
  .brand-panel {
    position: absolute;
    left: 0; top: 44px;
    width: 236px; height: 228px;
    background: var(--brand-blue);
    border-radius: 0 114px 114px 0;
  }
  .card--back .brand-name {
    left: 26px; top: 50%;
    transform: translateY(-50%);
    color: var(--white);
    font-size: 16px;
    width: 180px;
  }
  .card--back .brand-mark { background: var(--white); }
  .contact-block {
    position: absolute;
    left: 262px; top: 38px;
    color: var(--ink-blue);
  }
  .person-name {
    font-family: "Roboto Condensed", "Arial Narrow", sans-serif;
    font-weight: 700;
    font-size: 23px;
    letter-spacing: 0.3px;
  }
  .person-title { font-size: 11px; margin: 0 0 14px 4px; }
  .contact-row {
    display: flex;
    align-items: center;
    gap: 10px;
    font-size: 13px;
    line-height: 1.15;
    margin-bottom: 12px;
  }
  .contact-icon {
    width: 26px; height: 26px;
    flex: none;
    border-radius: 50%;
    background: var(--brand-blue);
    display: flex; align-items: center; justify-content: center;
  }
</style>
</head>
<body>

  <section class="card card--front" aria-label="Business card front">
    <div class="card-texture" role="img" aria-label="Faint light grey low-poly background texture"></div>
    <div class="edge-bar edge-bar--right"></div>
    <div class="edge-bar edge-bar--left"></div>
    <div class="brand-name"><span class="brand-mark"></span>Carver Lindqvist Group</div>
  </section>

  <section class="card card--back" aria-label="Business card back">
    <div class="card-texture" role="img" aria-label="Faint light grey low-poly background texture"></div>
    <div class="brand-panel">
      <div class="brand-name"><span class="brand-mark"></span>Carver Lindqvist Group</div>
    </div>
    <div class="contact-block">
      <h1 class="person-name">RAY PEMBERLY, CPA</h1>
      <p class="person-title">Partner and Managing Director</p>

      <div class="contact-row">
        <span class="contact-icon">
          <svg width="14" height="14" viewBox="0 0 14 14" fill="none" stroke="#fff" stroke-width="1.4" stroke-linejoin="round"><path d="M2 7 L7 2.5 L12 7 M3.5 6 V12 H10.5 V6"/></svg>
        </span>
        <span>8282 Orchard Vale Rd. Suite 610<br>Dallas, TX 75391</span>
      </div>

      <div class="contact-row">
        <span class="contact-icon">
          <svg width="14" height="14" viewBox="0 0 14 14" fill="none" stroke="#fff" stroke-width="1.3" stroke-linejoin="round"><rect x="2" y="3.5" width="10" height="7"/><path d="M2 3.5 L7 7.5 L12 3.5"/></svg>
        </span>
        <span>ray@carverlindqvist.example</span>
      </div>

      <div class="contact-row">
        <span class="contact-icon">
          <svg width="14" height="14" viewBox="0 0 14 14" fill="#fff"><path d="M3.2 1.8 L5.2 1.8 L6 4.6 L4.8 5.6 C5.5 7.2 6.8 8.5 8.4 9.2 L9.4 8 L12.2 8.8 L12.2 10.8 C12.2 11.6 11.6 12.2 10.8 12.2 C6 12 2 8 1.8 3.2 C1.8 2.4 2.4 1.8 3.2 1.8 Z"/></svg>
        </span>
        <span>O 214-555-0184<br>M 214-555-0237</span>
      </div>

      <div class="contact-row">
        <span class="contact-icon">
          <svg width="14" height="14" viewBox="0 0 14 14" fill="none" stroke="#fff" stroke-width="1.1"><circle cx="7" cy="7" r="5"/><ellipse cx="7" cy="7" rx="2.2" ry="5"/><path d="M2 7 H12"/></svg>
        </span>
        <span>www.carverlindqvist.example</span>
      </div>
    </div>
  </section>

</body>
</html>
```